Enlargement project

We would like to create an enlargement of the attached business card design, so that we are able to print hi-res business cards from it,

The end result we are after is an illustrator template that contains hi-res graphics and text that we can edit to insert people's names, job titles, phone and email details

The two colours used within the design are:

Pantone 350 (green)
Panton 484 (red)

The fonts used are;

Futura Medium
Futura Bk BT Italic

```html
<!DOCTYPE html>
<html lang="en">
<head>
<meta charset="utf-8">
<title>Keepwell — Business Card</title>
<link rel="stylesheet" href="https://fonts.googleapis.com/css2?family=Jost:ital,wght@0,400;0,500;1,400&display=swap">
<style>
  :root {
    --brand-green: #0f4a2a;
    --brand-red: #9a2a1c;
    --card-border: #c4c4c4;
    --page-bg: #ffffff;
    --card-bg: #ffffff;
  }
  * { margin: 0; padding: 0; box-sizing: border-box; }
  html, body {
    width: 1200px;
    height: 900px;
    overflow: hidden;
    background: var(--page-bg);
  }
  body {
    position: relative;
    font-family: "Jost", "Futura", sans-serif;
    font-weight: 500;
    color: var(--brand-green);
  }
  .business-card {
    position: absolute;
    left: 248px;
    top: 248px;
    width: 704px;
    height: 404px;
    background: var(--card-bg);
    border: 2px solid var(--card-border);
  }
  .brand-name {
    position: absolute;
    left: 45px;
    top: 70px;
    font-size: 46px;
    font-weight: 500;
    line-height: 1;
    color: var(--brand-green);
  }
  .address,
  .phone-list,
  .email {
    position: absolute;
    left: 45px;
    font-size: 17px;
    line-height: 21px;
    list-style: none;
    font-style: normal;
  }
  .address { top: 203px; }
  .phone-list { top: 278px; }
  .phone-label { display: inline-block; width: 21px; }
  .email { top: 350px; }
  .person {
    position: absolute;
    left: 464px;
    top: 205px;
    color: var(--brand-red);
  }
  .person-name {
    font-size: 27px;
    font-style: italic;
    font-weight: 400;
    line-height: 30px;
  }
  .person-title {
    font-size: 17.5px;
    font-weight: 400;
    line-height: 20px;
  }
  .website {
    position: absolute;
    right: 46px;
    top: 350px;
    font-size: 17px;
    line-height: 21px;
  }
</style>
</head>
<body>
  <main class="business-card">
    <p class="brand-name">Keepwell</p>

    <address class="address">
      Suite 4, Level 2<br>
      45 Sample Road<br>
      Sydney NSW 2000
    </address>

    <ul class="phone-list">
      <li><span class="phone-label">t:</span>02 5550 0140</li>
      <li><span class="phone-label">f:</span>02 5550 0141</li>
      <li><span class="phone-label">d:</span>02 5550 0142</li>
    </ul>

    <p class="email">dlee@keepwell.net</p>

    <div class="person">
      <p class="person-name">Daniel</p>
      <p class="person-title">Technical Operations</p>
    </div>

    <p class="website">www.keepwell.net</p>
  </main>
</body>
</html>
```